Cybersecurity company is looking for business card.

I need a business card design for our company, we are a cybersecurity company providing advance technology to protect agains any kind of malware. We need a fresh modern design it should communicate modern, technology and growth.

Target Market(s)

Business to business

Industry/Entity Type

Business

Contact Information for Business Card

Should have location, address, fax, mobile, phone, email and website.

Requirements
Must have
• Must follow company's logo color and style. Must have the company's log on its.

```html
<!DOCTYPE html>
<html lang="en">
<head>
<meta charset="utf-8">
<title>Vexora business card</title>
<link rel="stylesheet" href="https://fonts.googleapis.com/css2?family=Open+Sans:wght@400;700&display=swap">
<style>
  :root {
    --ink: #000000;
    --paper: #ffffff;
    --crimson: #a00f0f;
    --signal-red: #e8141a;
    --icon-red: #d9402e;
    --icon-orange: #f0683a;
  }
  html, body {
    margin: 0;
    padding: 0;
    width: 992px;
    height: 1200px;
    overflow: hidden;
    background: var(--paper);
  }
  .sheet { display: block; width: 992px; height: 1200px; }
  .fill-ink { fill: var(--ink); }
  .fill-paper { fill: var(--paper); }
  .fill-crimson { fill: var(--crimson); }
  .brand-name {
    font-family: "Open Sans", sans-serif;
    font-weight: 700;
    fill: var(--ink);
  }
  .contact-line {
    font-family: "Open Sans", sans-serif;
    font-weight: 400;
    font-size: 40px;
    fill: var(--signal-red);
  }
  .icon-fill { fill: var(--icon-red); }
  .icon-orange { fill: var(--icon-orange); }
  .icon-line { fill: none; stroke: var(--icon-orange); stroke-width: 3; stroke-linejoin: round; }
</style>
</head>
<body>
<svg class="sheet" viewBox="0 0 1200 1452" preserveAspectRatio="none" xmlns="http://www.w3.org/2000/svg">

  <!-- Front of card -->
  <g class="card card-front">
    <rect class="fill-ink" x="5" y="3" width="1193" height="701"/>
    <polygon class="fill-paper" points="283,3 555,3 513,57 1195,57 1195,285 333,285 283,350"/>
    <polygon class="fill-crimson" points="5,704 283,704 283,350"/>
    <text class="brand-name" x="352" y="235" font-size="210" textLength="758" lengthAdjust="spacingAndGlyphs">vexora</text>
  </g>

  <!-- Back of card -->
  <g class="card card-back">
    <rect class="fill-ink" x="3" y="750" width="1195" height="700"/>
    <polygon class="fill-paper" points="279,750 497,750 453,813 861,813 861,936 366,936 279,1060"/>
    <polygon class="fill-crimson" points="3,1450 279,1450 279,1060"/>
    <text class="brand-name" x="360" y="912" font-size="118" textLength="423" lengthAdjust="spacingAndGlyphs">vexora</text>

    <g class="contact-icons">
      <!-- location pin -->
      <path class="icon-fill" d="M336 1038 a13 13 0 0 1 13 13 c0 10 -13 25 -13 25 c0 0 -13 -15 -13 -25 a13 13 0 0 1 13 -13z"/>
      <circle class="fill-ink" cx="336" cy="1051" r="4"/>
      <!-- address card -->
      <rect class="icon-fill" x="318" y="1099" width="38" height="26" rx="2"/>
      <rect class="fill-paper" x="318" y="1099" width="38" height="5"/>
      <!-- mobile -->
      <rect class="icon-fill" x="326" y="1146" width="25" height="41" rx="4"/>
      <rect class="fill-paper" x="330" y="1152" width="17" height="27"/>
      <rect class="icon-fill" x="333" y="1156" width="11" height="19"/>
      <!-- phone handset -->
      <path class="icon-orange" d="M324 1205 c4 -3 8 -2 10 2 l4 7 c1 3 0 5 -3 7 c3 6 8 11 14 14 c2 -3 4 -4 7 -3 l7 4 c4 2 5 6 2 10 c-4 5 -10 5 -16 1 c-11 -7 -20 -16 -26 -27 c-3 -6 -3 -11 1 -15z"/>
      <!-- fax -->
      <circle class="icon-orange" cx="338" cy="1274" r="18"/>
      <rect class="fill-paper" x="327" y="1267" width="22" height="14" rx="2" opacity="0.85"/>
      <rect class="icon-orange" x="331" y="1271" width="7" height="6"/>
      <!-- plain envelope -->
      <rect class="icon-line" x="318" y="1318" width="38" height="25" rx="2"/>
      <path class="icon-line" d="M319 1320 l18 13 l18 -13"/>
      <!-- at sign -->
      <text x="339" y="1395" font-family="Open Sans, sans-serif" font-size="40" class="icon-orange" text-anchor="middle">@</text>
    </g>

    <g class="contact-details">
      <text class="contact-line" x="390" y="1072">Port Avalen - Norland</text>
      <text class="contact-line" x="388" y="1125">Harbor Tech Park (HTP) -Meridian Road.</text>
      <text class="contact-line" x="388" y="1177">+44 555 010 2468</text>
      <text class="contact-line" x="393" y="1230">02 555 0135</text>
      <text class="contact-line" x="393" y="1282">02 555 0179</text>
      <text class="contact-line" x="388" y="1335">name.surname@vexora.com</text>
      <text class="contact-line" x="393" y="1388">www.vexora.com</text>
    </g>
  </g>
</svg>
</body>
</html>
```